Crowler Can Label for a Brewery Beer Can

Creating a label for our brewery's Crowler Can. Our area is know for mountains, glaciers, and the ocean view. We would like to include these in the drawing. Along with our logo. Overall we think more is less. A nice simple label is our preference that is elegant. We included a couple we like, but do not copy them exactly.

There will need to be white room for us to label each can by hand - spaces for - Name, ABV and Date.

The text must be on lable- GOVERNMENT WARNING: (1) According to the Surgeon General, women should not drink alcoholic beverages during pregnancy because of the risk of birth defects. (2) Consumption of alcoholic beverages impairs your ability to drive a car or operate machinery,and may cause health problems.

We also want our address and website-
287 Torrin Dr, Valdez Alaska 99686
www.hollowmarchales.com

Also needs to have size on the label - 32 Fluid Oz

Getting some great designs, but be good for more time for some designers to rework with suggestions given.

Colors

Designer to choose colors to be used in the design.

Requirements
Must have
• I included the label size template in the graphics. Must be this size.
• There will need to be white room for us to label each can by hand - spaces for - Name, ABV and Date.
• The text must be on lable- GOVERNMENT WARNING: (1) According to the Surgeon General, women should not drink alcoholic beverages during pregnancy because of the risk of birth defects. (2) Consumption of alcoholic beverages impairs your ability to drive a car or operate machinery,and may cause health problems.
• We also want our address and website-
• 287 Torrin Dr, Valdez Alaska 99686
• www.hollowmarchales.com
• Needs to have size on the label - 32 Fl Oz
Nice to have
• Mountains, Glacier and ocean scene.

```html
<!DOCTYPE html>
<html lang="en">
<head>
<meta charset="UTF-8">
<title>Hollow March Ales – Brewery's Crowler Label</title>
<link href="https://fonts.googleapis.com/css2?family=Archivo+Black&family=Great+Vibes&family=Kalam:wght@700&family=Open+Sans:wght@400;600;700&family=Roboto+Slab:wght@700&display=swap" rel="stylesheet">
<style>
  :root {
    --backdrop: #d4d1ec;
    --label-top: #c9c8e2;
    --label-mid: #8b86b8;
    --label-deep: #5e5790;
    --ink-light: #e9e8f4;
    --ink-dark: #2a1f52;
    --field-white: #f4f3fa;
    --scene-sky: #7d78ad;
    --scene-haze: #b9b7d6;
    --scene-forest: #3a2430;
  }
  * { box-sizing: border-box; margin: 0; padding: 0; }
  html, body { width: 1200px; height: 900px; overflow: hidden; }
  body {
    background: var(--backdrop);
    position: relative;
    font-family: "Open Sans", sans-serif;
  }
  .label-panel {
    position: absolute;
    top: 90px;
    width: 360px;
    height: 720px;
    border-radius: 18px;
    overflow: hidden;
    background: linear-gradient(180deg, var(--label-top) 0%, var(--label-mid) 30%, var(--label-deep) 60%);
  }
  .label-front { left: 180px; }
  .label-back { left: 660px; }

  .mountain-scene {
    position: absolute;
    left: 0; right: 0; bottom: 0;
    background: linear-gradient(180deg, rgba(125,120,173,0) 0%, var(--scene-haze) 28%, var(--scene-sky) 55%, var(--label-deep) 72%, var(--scene-forest) 100%);
  }
  .label-front .mountain-scene { top: 430px; }
  .label-back .mountain-scene { top: 500px; }

  /* Front */
  .brand-mark {
    position: absolute;
    top: 52px;
    left: 145px;
    width: 70px;
    height: 70px;
    border-radius: 50%;
    background: var(--ink-light);
    opacity: 0.85;
  }
  .brand-block {
    position: absolute;
    top: 138px; left: 0; right: 0;
    text-align: center;
    color: var(--ink-light);
  }
  .brand-name {
    font-family: "Roboto Slab", serif;
    font-weight: 700;
    font-size: 34px;
    line-height: 1.1;
    letter-spacing: 1px;
  }
  .brand-location {
    margin-top: 10px;
    font-family: "Open Sans", sans-serif;
    font-size: 11px;
    letter-spacing: 2px;
    display: flex;
    align-items: center;
    justify-content: center;
    gap: 8px;
  }
  .brand-location::before, .brand-location::after {
    content: "";
    width: 22px;
    height: 1px;
    background: var(--ink-light);
  }
  .product-title {
    position: absolute;
    top: 290px; left: 0; right: 0;
    text-align: center;
    font-family: "Great Vibes", cursive;
    font-weight: 400;
    font-size: 50px;
    line-height: 1.2;
    color: var(--ink-light);
    white-space: nowrap;
  }
  .volume {
    position: absolute;
    top: 372px; left: 0; right: 0;
    text-align: center;
    font-family: "Kalam", cursive;
    font-weight: 700;
    font-size: 19px;
    color: var(--ink-light);
  }

  /* Back */
  .write-field {
    position: absolute;
    left: 18px; right: 18px;
    height: 80px;
    border-radius: 16px;
    background: var(--field-white);
    padding-left: 16px;
    display: flex;
    align-items: center;
    font-family: "Archivo Black", sans-serif;
    font-size: 16px;
    color: var(--ink-dark);
  }
  .field-name { top: 30px; }
  .field-abv { top: 130px; }
  .field-date { top: 230px; }
  .contact {
    position: absolute;
    top: 324px; left: 0; right: 0;
    text-align: center;
    font-size: 12.5px;
    font-weight: 600;
    line-height: 1.5;
    color: var(--ink-light);
  }
  .warning-box {
    position: absolute;
    top: 370px; left: 18px; right: 18px;
    border-radius: 22px;
    background: rgba(244,243,250,0.88);
    padding: 10px 16px 12px;
    color: var(--ink-dark);
    font-size: 12.3px;
    line-height: 1.6;
    text-align: justify;
  }
  .warning-title {
    display: block;
    text-align: center;
    font-weight: 700;
    font-size: 13px;
  }
</style>
</head>
<body>
  <section class="label-panel label-front" aria-label="Front of crowler label">
    <div class="mountain-scene" role="img" aria-label="Night scene of clouds, mountains, bay and spruce forest under falling snow"></div>
    <div class="brand-mark" aria-hidden="true"></div>
    <div class="brand-block">
      <p class="brand-name">HOLLOW MARCH<br>ALES</p>
      <p class="brand-location">VALDEZ, ALASKA</p>
    </div>
    <h1 class="product-title">Brewery's Crowler</h1>
    <p class="volume">32 FLUID OZ</p>
  </section>

  <section class="label-panel label-back" aria-label="Back of crowler label">
    <div class="mountain-scene" role="img" aria-label="Night scene of clouds, mountains, bay and spruce forest under falling snow"></div>
    <div class="write-field field-name">NAME:</div>
    <div class="write-field field-abv">ABV:</div>
    <div class="write-field field-date">DATE:</div>
    <p class="contact">287 Torrin Dr, Valdez Alaska 99686<br>www.hollowmarchales.com</p>
    <div class="warning-box">
      <span class="warning-title">GOVERNMENT WARNING:</span>
      (1) According to the Surgeon General, women should not drink alcoholic beverages during pregnancy because of the risk of birth defects. (2) Consumption of alcoholic beverages impairs your ability to drive a car or operate machinery, and may cause health problems.
    </div>
  </section>
</body>
</html>
```